Looking for a new business card design

We are looking for a corporate looking yet still a bit different then the rest. I would like the card black with the picture on the back and the phrase "Lighting the way to goal ZERO" on the back as well. Then a clean look on the front with a bit of an edge.

Target Market(s)

Corporate oil executives and drilling supervisors

Industry/Entity Type

Oil And Gas

Contact Information for Business Card

Black, bold, clean lines.

Font styles to use
Sans Serif

Requirements
Must have
• Picture on the back with the slogan "Lighting the way to goal ZERO"
• Black background
• Stands out

```html
<!DOCTYPE html>
<html lang="en">
<head>
<meta charset="utf-8">
<title>Halcyon Energy Services Corp — Business Card</title>
<link rel="stylesheet" href="https://fonts.googleapis.com/css2?family=PT+Sans:wght@400;700&display=swap">
<style>
  :root {
    --stage: #5a5a5a;
    --card: #000000;
    --lime: #c3d22b;
    --grey: #6d6e71;
    --white: #ffffff;
    --band: rgba(90, 90, 80, 0.55);
  }
  * { box-sizing: border-box; margin: 0; padding: 0; }
  html, body {
    width: 1200px; height: 1200px; overflow: hidden;
    background: var(--stage);
    font-family: "PT Sans", sans-serif;
  }
  .card {
    position: absolute;
    width: 715px; height: 405px;
    border-radius: 18px;
    background: var(--card);
    overflow: hidden;
  }
  .card--front { left: 242px; top: 170px; }
  .card--back  { left: 244px; top: 626px; }

  .brand { position: absolute; left: 488px; top: 86px; }
  .brand__name {
    color: var(--lime); font-weight: 700; font-size: 46px;
    line-height: 1; letter-spacing: 0.5px;
  }
  .brand__tagline {
    color: var(--grey); font-size: 20px; line-height: 1; margin-top: 8px;
  }

  .person__bar {
    position: absolute; left: 0; top: 219px; width: 14px; height: 46px;
    background: var(--lime);
  }
  .person { position: absolute; left: 33px; top: 217px; }
  .person__name { color: var(--white); font-weight: 700; font-size: 28px; line-height: 1.1; }
  .person__role { color: var(--lime); font-size: 18px; line-height: 1.2; margin-top: 2px; }

  .contact { position: absolute; left: 33px; top: 298px; list-style: none; }
  .contact__item {
    display: flex; align-items: center; height: 24px;
    color: var(--white); font-size: 18px;
  }
  .contact__icon { width: 20px; height: 16px; margin-right: 10px; flex: none; }

  .photo {
    position: absolute; inset: 0;
    background:
      radial-gradient(ellipse 45% 30% at 36% 14%, rgba(255,255,255,0.55), transparent 70%),
      radial-gradient(ellipse 70% 55% at 50% 72%, #8d8160 0%, #5d553f 40%, #1c1a14 75%, #050505 100%);
  }
  .slogan-band {
    position: absolute; left: 0; top: 274px; width: 100%; height: 35px;
    background: var(--band);
  }
  .slogan {
    position: absolute; left: 162px; top: 274px; height: 35px;
    display: flex; align-items: center;
    color: var(--lime); font-size: 21px;
  }
  .slogan strong { font-weight: 700; margin-left: 5px; }
</style>
</head>
<body>
  <section class="card card--front">
    <div class="brand">
      <div class="brand__name">HALCYON</div>
      <div class="brand__tagline">Energy Services Corp</div>
    </div>

    <div class="person__bar"></div>
    <div class="person">
      <div class="person__name">Daniel Reyes</div>
      <div class="person__role">CEO</div>
    </div>

    <ul class="contact">
      <li class="contact__item">
        <svg class="contact__icon" viewBox="0 0 20 16" aria-hidden="true">
          <path d="M1 5 Q10 -1 19 5 L16 7 L14 5 Q10 3.5 6 5 L4 7 Z" fill="#c3d22b"/>
          <rect x="3" y="8" width="14" height="7" rx="1.5" fill="#c3d22b"/>
          <circle cx="10" cy="11.5" r="2" fill="#000"/>
        </svg>
        (00) 000-0000
      </li>
      <li class="contact__item">
        <svg class="contact__icon" viewBox="0 0 20 16" aria-hidden="true">
          <rect x="1" y="3" width="18" height="11" fill="#c3d22b"/>
          <path d="M1 3 L10 10 L19 3 M1 14 L8 8 M19 14 L12 8" stroke="#000" stroke-width="1.3" fill="none"/>
        </svg>
        dreyes@halcyonesc.com
      </li>
      <li class="contact__item">
        <svg class="contact__icon" viewBox="0 0 20 16" aria-hidden="true">
          <g fill="none" stroke="#c3d22b" stroke-width="1.3">
            <circle cx="10" cy="8" r="7"/>
            <ellipse cx="10" cy="8" rx="3" ry="7"/>
            <path d="M3 8 H17 M4.2 4.5 H15.8 M4.2 11.5 H15.8"/>
          </g>
        </svg>
        www.halcyonesc.com
      </li>
    </ul>
  </section>

  <section class="card card--back">
    <div class="photo" role="img" aria-label="Aerial night photograph of a brightly lit drilling rig site surrounded by dark forest"></div>
    <div class="slogan-band"></div>
    <p class="slogan">Lighting the way to goal <strong>ZERO</strong></p>
  </section>
</body>
</html>
```